Create for us a Shop-Stopper Business Card

We need a standout, first class business card to go along with our new brand strategy. Sleek, Contemporary and fresh.

Colors and theme must sync with our websitewww.pelvorpower.co.uk

We want a business card that has a global brand appeal. TKR Energy is a small UK renewable company that specialises in energy projects in Africa. We want a business card that has the following characteristics: Very short, precise, global, stand out, NOT TOO LOUD but contemporary. The company's colour themes are White, Grey with a hint of green.

Target Market(s)

Business exec, high net worth individuals, investors, commercial leaders, suppliers, government officials

Industry/Entity Type

Solar Energy

Contact Information for Business Card

Logo, Name, Title, Address, web address, email,

Requirements
Must have
• Logo must be sharp
Nice to have
• Adapt fonts from the logo. The large circular side of the logo at the back in a very refreshing way
Should not have
• No solar panel shapes or image.Very little black. If possible avoid black. Its not coming out nice. I think !!!

```html
<!DOCTYPE html>
<html lang="en">
<head>
<meta charset="utf-8">
<title>TKR Energy – Business Card</title>
<link href="https://fonts.googleapis.com/css2?family=Questrial&family=Arimo:wght@400;700&display=swap" rel="stylesheet">
<style>
  :root {
    --page-bg: #e9ebea;
    --green-deep: #0f6b2a;
    --green-mid: #1f9a3c;
    --green-bright: #3fbf4a;
    --green-lime: #9ed13a;
    --green-band: #2a9a3e;
    --slate-dark: #2b2c2e;
    --slate-mid: #4a4b4e;
    --white: #ffffff;
    --text-light: #f2f2f2;
    --logo-grey: #4d4d4f;
    --accent-name: #3fb34f;
  }
  * { margin: 0; padding: 0; box-sizing: border-box; }
  html, body {
    width: 1200px;
    height: 843px;
    overflow: hidden;
    background: var(--page-bg);
  }
  .canvas {
    position: relative;
    width: 1200px;
    height: 843px;
  }
  .card {
    position: absolute;
    top: 273px;
    width: 520px;
    height: 297px;
    border-radius: 4px;
    overflow: hidden;
    box-shadow: 0 6px 18px rgba(0,0,0,0.18);
  }

  /* Brand side */
  .card--brand {
    left: 60px;
    background: radial-gradient(ellipse at 42% 40%, var(--green-bright) 0%, var(--green-mid) 40%, var(--green-deep) 100%);
  }
  .brand-lockup {
    position: absolute;
    left: 60px;
    top: 108px;
    display: flex;
    align-items: center;
    gap: 14px;
  }
  .brand-lockup__dot {
    width: 46px;
    height: 46px;
    border-radius: 50%;
    background: var(--white);
  }
  .brand-lockup__name {
    font-family: "Questrial", sans-serif;
    font-size: 44px;
    letter-spacing: 1px;
    color: var(--white);
  }
  .brand-web {
    position: absolute;
    left: 0;
    right: 0;
    bottom: 52px;
    text-align: center;
    font-family: "Arimo", sans-serif;
    font-size: 13px;
    letter-spacing: 4px;
    color: var(--text-light);
  }

  /* Contact side */
  .card--contact {
    left: 620px;
    background: linear-gradient(160deg, var(--slate-mid) 0%, var(--slate-dark) 70%);
  }
  .card__shapes {
    position: absolute;
    inset: 0;
  }
  .contact-block {
    position: absolute;
    left: 34px;
    top: 34px;
    font-family: "Arimo", sans-serif;
    color: var(--text-light);
  }
  .contact-block__name {
    font-size: 17px;
    color: var(--accent-name);
  }
  .contact-block__title {
    font-size: 12.5px;
    margin-top: 4px;
  }
  .contact-block__address {
    font-size: 12px;
    line-height: 16px;
    margin-top: 26px;
  }
  .contact-list {
    list-style: none;
    margin-top: 10px;
  }
  .contact-list li {
    display: flex;
    align-items: center;
    gap: 8px;
    font-size: 12px;
    line-height: 19px;
  }
  .contact-list svg { width: 11px; height: 11px; flex: none; }
  .contact-lockup {
    position: absolute;
    left: 300px;
    top: 128px;
    display: flex;
    align-items: center;
    gap: 8px;
  }
  .contact-lockup__dot {
    width: 30px;
    height: 30px;
    border-radius: 50%;
    background: var(--green-band);
  }
  .contact-lockup__name {
    font-family: "Questrial", sans-serif;
    font-size: 27px;
    color: var(--logo-grey);
  }
</style>
</head>
<body>
<main class="canvas">

  <section class="card card--brand" aria-label="Card brand side">
    <div class="brand-lockup">
      <span class="brand-lockup__dot"></span>
      <span class="brand-lockup__name">TKR ENERGY</span>
    </div>
    <p class="brand-web">www.pelvorpower.co.uk</p>
  </section>

  <section class="card card--contact" aria-label="Card contact side">
    <svg class="card__shapes" viewBox="0 0 520 297" preserveAspectRatio="none" aria-hidden="true">
      <path d="M338 0 C262 60 238 180 250 297 L520 297 L520 0 Z" fill="var(--green-lime)"/>
      <path d="M356 0 C282 62 252 180 256 297 L520 297 L520 0 Z" fill="var(--green-band)"/>
      <path d="M378 0 C300 64 260 180 262 297 L520 297 L520 0 Z" fill="var(--white)"/>
    </svg>

    <div class="contact-block">
      <p class="contact-block__name">Alan Mercer</p>
      <p class="contact-block__title">President</p>
      <p class="contact-block__address">7261 Kensington Drive<br>Glen Oaks, NY 11004</p>
      <ul class="contact-list">
        <li>
          <svg viewBox="0 0 12 12"><path d="M2 1h3l1 3-1.5 1a6 6 0 0 0 2.5 2.5L8 6l3 1v3a1 1 0 0 1-1 1A9 9 0 0 1 1 2a1 1 0 0 1 1-1z" fill="var(--accent-name)"/></svg>
          481 6392 7105
        </li>
        <li>
          <svg viewBox="0 0 12 12"><rect x="0.5" y="2" width="11" height="8" rx="1" fill="var(--accent-name)"/><path d="M1 2.5l5 4 5-4" stroke="var(--slate-dark)" fill="none"/></svg>
          alan@pelvorpower.co.uk
        </li>
        <li>
          <svg viewBox="0 0 12 12"><circle cx="6" cy="6" r="5.5" fill="var(--accent-name)"/><path d="M0.5 6h11M6 0.5c-3 3-3 8 0 11M6 0.5c3 3 3 8 0 11" stroke="var(--slate-dark)" stroke-width="0.8" fill="none"/></svg>
          www.pelvorpower.co.uk
        </li>
      </ul>
    </div>

    <div class="contact-lockup">
      <span class="contact-lockup__dot"></span>
      <span class="contact-lockup__name">TKR ENERGY</span>
    </div>
  </section>

</main>
</body>
</html>
```